Web App UI Design prototype

I have a sketch of a series of pages for a new web app, and would like to develop a clean, user friendly, intuitive design around the content.

Target Market(s)

small to medium sized business owners

Number of Pages Required

5+ page

Font styles to use
Sans Serif

Colors
33a6d7
85cae6
33b8a4
86cfc6
886aae
faa54b
000000
757575
cbcbcb

Requirements
Must have
• Color pallet that fits with my logo
• Clean modern, timeless design
• Intuitive use of UI
• Icons always help

```html
<!DOCTYPE html>
<html lang="en">
<head>
<meta charset="utf-8">
<title>Verdia – Dashboard</title>
<link href="https://fonts.googleapis.com/css2?family=Open+Sans:wght@300;400;600;700&display=swap" rel="stylesheet">
<style>
:root{
  --blue:#33a6d7;
  --blue-light:#85cae6;
  --teal:#33b8a4;
  --teal-light:#86cfc6;
  --purple:#886aae;
  --orange:#faa54b;
  --ink:#000000;
  --grey:#757575;
  --grey-light:#cbcbcb;
  --sidebar:#1d2738;
  --sidebar-line:#36415a;
  --sidebar-text:#c3c8d1;
  --page:#e6eaed;
  --strip:#f4f5f6;
  --card-head:#f7f7f7;
  --line:#e4e6e8;
  --text:#333a44;
}
*{box-sizing:border-box;margin:0;padding:0}
html,body{width:1200px;height:926px;overflow:hidden}
body{font-family:"Open Sans",Arial,sans-serif;background:var(--page);color:var(--text);position:relative}
.abs{position:absolute}

/* header */
.topbar{position:absolute;left:0;top:0;width:1200px;height:82px;background:#fff;box-shadow:0 1px 4px rgba(0,0,0,.08);z-index:2}
.brand{position:absolute;left:26px;top:22px;display:flex;align-items:center;gap:10px}
.brand-mark{width:20px;height:20px;border-radius:50%;background:var(--teal)}
.brand-name{font-size:31px;font-weight:400;color:var(--teal);letter-spacing:.5px;line-height:38px}
.divider-v{position:absolute;top:0;width:1px;height:82px;background:var(--line)}
.menu-icon{left:260px;top:34px}
.crumb{left:337px;top:32px;font-size:13px;color:var(--text);display:flex;align-items:center;gap:6px}
.search{left:614px;top:32px;font-size:12px;font-style:italic;color:var(--grey-light);display:flex;align-items:center;gap:12px}
.user{left:928px;top:21px;display:flex;align-items:center;gap:12px;font-size:13px;color:var(--text)}
.avatar{width:40px;height:40px;border-radius:50%;background:radial-gradient(circle at 50% 45%,#c98a6a,#6e4a3a);border:2px solid #e8e8e8}
.user .chev{margin-left:50px}
.gear{left:1140px;top:33px}

/* sidebar */
.sidebar{position:absolute;left:0;top:82px;width:235px;height:844px;background:var(--sidebar);color:var(--sidebar-text)}
.run-btn{position:absolute;left:32px;top:26px;width:84px;height:34px;background:var(--teal);border-radius:2px;color:#fff;font-size:13px;font-weight:600;display:flex;align-items:center;justify-content:center;gap:8px}
.side-rule{position:absolute;left:24px;width:187px;height:1px;background:var(--sidebar-line)}
.side-head{position:absolute;left:33px;width:172px;font-size:13px;display:flex;justify-content:space-between;align-items:center}
.side-head.active{color:#fff}
.tree{position:absolute;left:54px;border-left:1px solid var(--sidebar-line)}
.tree li{list-style:none;position:relative;padding-left:16px;font-size:13px;height:24px;line-height:24px}
.tree li.current{color:var(--blue)}
.tree li.current::before{content:"";position:absolute;left:0;top:12px;width:8px;height:1px;background:var(--blue)}
.footnote{position:absolute;left:24px;top:782px;font-size:12px;line-height:17px;color:var(--sidebar-text)}

/* title strip */
.title-strip{position:absolute;left:235px;top:82px;width:965px;height:86px;background:var(--strip)}
.page-title{position:absolute;left:23px;top:26px;font-size:26px;font-weight:300;color:#8a8f96}
.filter{position:absolute;top:30px;height:29px;border:1px solid var(--grey-light);background:#fff;font-size:12px;color:var(--text);display:flex;align-items:center;justify-content:space-between;padding:0 12px 0 15px}

/* cards */
.card{position:absolute;background:#fff;box-shadow:0 1px 2px rgba(0,0,0,.05)}
.card-head{height:43px;background:var(--card-head);display:flex;align-items:center;justify-content:space-between;padding:0 25px;font-size:13px;color:var(--text);letter-spacing:.3px}
.legend{display:flex;gap:22px;font-size:12.5px;letter-spacing:0}
.legend span{display:flex;align-items:center;gap:10px}
.dot{width:11px;height:11px;border-radius:50%;border:2px solid currentColor;position:relative}
.dot::after{content:"";position:absolute;inset:2px;border-radius:50%;background:currentColor}
.range{font-size:12.5px;color:#9a9fa5;display:flex;align-items:center;gap:10px;letter-spacing:0}

.donuts{position:absolute;left:24px;top:75px;display:flex;gap:25px}
.donut{width:116px;text-align:center}
.donut-ring{position:relative;width:116px;height:116px}
.donut-value{position:absolute;inset:0;display:flex;align-items:center;justify-content:center;font-size:31px;font-weight:300}
.donut-value sup{font-size:14px;margin-top:-14px}
.donut-label{margin-top:20px;font-size:13px;color:#8d9298}
.note-rule{position:absolute;left:25px;top:258px;width:396px;height:1px;background:var(--line)}
.note{position:absolute;left:25px;top:277px;width:396px;text-align:center}
.note h4{font-size:12.5px;font-weight:600;color:var(--text)}
.note p{font-size:12px;line-height:20px;color:#9a9fa5;margin-top:3px}

.total{position:absolute;left:0;width:445px;top:272px;line-height:42px;text-align:center;font-size:31px;font-weight:400;color:var(--blue)}
.delta{position:absolute;left:0;width:445px;top:314px;line-height:18px;text-align:center;font-size:12px;color:var(--text)}
.delta .arrow{font-size:9px;color:var(--text);margin-right:4px}
</style>
</head>
<body>

<header class="topbar">
  <div class="brand"><span class="brand-mark"></span><span class="brand-name">verdia</span></div>
  <div class="divider-v" style="left:574px"></div>
  <div class="divider-v" style="left:886px"></div>
  <div class="divider-v" style="left:1096px"></div>

  <svg class="abs menu-icon" width="17" height="14" viewBox="0 0 17 14"><g stroke="#33b8a4" stroke-width="1.6"><line x1="0" y1="1" x2="17" y2="1"/><line x1="0" y1="7" x2="17" y2="7"/><line x1="0" y1="13" x2="17" y2="13"/></g></svg>

  <div class="abs crumb">
    <svg width="13" height="12" viewBox="0 0 13 12"><path d="M6.5 0L0 6h2v6h3.5V8h2v4H11V6h2z" fill="#33b8a4"/></svg>
    <span>Home / Dashboard</span>
  </div>

  <div class="abs search">
    <svg width="14" height="14" viewBox="0 0 14 14"><circle cx="8" cy="6" r="4.6" fill="none" stroke="#33b8a4" stroke-width="1.5"/><line x1="4.6" y1="9.4" x2="1" y2="13" stroke="#33b8a4" stroke-width="1.6"/></svg>
    <span>Search here ...</span>
  </div>

  <div class="abs user">
    <div class="avatar" role="img" aria-label="User profile photo"></div>
    <span>Maren</span>
    <svg class="chev" width="9" height="6" viewBox="0 0 9 6"><path d="M1 1l3.5 3.5L8 1" fill="none" stroke="#757575" stroke-width="1.3"/></svg>
  </div>

  <svg class="abs gear" width="16" height="16" viewBox="0 0 16 16"><g fill="#33a6d7"><circle cx="8" cy="8" r="5"/><rect x="6.6" y="0.5" width="2.8" height="15" rx="1"/><rect x="0.5" y="6.6" width="15" height="2.8" rx="1"/><rect x="6.6" y="0.5" width="2.8" height="15" rx="1" transform="rotate(45 8 8)"/><rect x="6.6" y="0.5" width="2.8" height="15" rx="1" transform="rotate(-45 8 8)"/></g><circle cx="8" cy="8" r="2.2" fill="#fff"/></svg>
</header>

<aside class="sidebar">
  <div class="run-btn">
    <svg width="17" height="17" viewBox="0 0 17 17"><circle cx="8.5" cy="8.5" r="7.4" fill="none" stroke="#fff" stroke-width="1.6"/><path d="M6.8 5.2v6.6l5-3.3z" fill="#fff"/></svg>
    RUN
  </div>
  <div class="side-rule" style="top:85px"></div>
  <div class="side-head active" style="top:105px"><span>DEPARTMENTS</span><svg width="8" height="5" viewBox="0 0 8 5"><path d="M1 1l3 3 3-3" fill="none" stroke="#c3c8d1" stroke-width="1.2"/></svg></div>
  <ul class="tree" style="top:144px">
    <li class="current">Sales &amp; Marketing</li>
    <li>Operations</li>
    <li>Finance</li>
    <li>Admin</li>
  </ul>
  <div class="side-rule" style="top:283px"></div>
  <div class="side-head" style="top:304px"><span>PROCESSES</span><svg width="8" height="5" viewBox="0 0 8 5"><path d="M1 1l3 3 3-3" fill="none" stroke="#c3c8d1" stroke-width="1.2"/></svg></div>
  <ul class="tree" style="top:344px">
    <li>All</li>
    <li>Saved</li>
    <li>Recent</li>
  </ul>
  <div class="side-rule" style="top:458px"></div>
  <div class="footnote">© 2017 Verdia.<br>All right reserved.</div>
</aside>

<section class="title-strip">
  <h1 class="page-title">Dashboard</h1>
  <div class="filter" style="left:471px;width:99px"><span>Dept</span><svg width="8" height="5" viewBox="0 0 8 5"><path d="M1 1l3 3 3-3" fill="none" stroke="#757575" stroke-width="1.2"/></svg></div>
  <div class="filter" style="left:577px;width:124px"><span>Statuses</span><svg width="8" height="5" viewBox="0 0 8 5"><path d="M1 1l3 3 3-3" fill="none" stroke="#757575" stroke-width="1.2"/></svg></div>
  <div class="filter" style="left:709px;width:123px"><span>Assignees</span><svg width="8" height="5" viewBox="0 0 8 5"><path d="M1 1l3 3 3-3" fill="none" stroke="#757575" stroke-width="1.2"/></svg></div>
  <div class="filter" style="left:841px;width:99px"><span>Date</span><svg width="8" height="5" viewBox="0 0 8 5"><path d="M1 1l3 3 3-3" fill="none" stroke="#757575" stroke-width="1.2"/></svg></div>
</section>

<section class="card" style="left:259px;top:192px;width:916px;height:330px">
  <div class="card-head">
    <span>STACKED AREA CHART</span>
    <div class="legend">
      <span><i class="dot" style="color:var(--orange)"></i>Stacked</span>
      <span><i class="dot" style="color:var(--purple)"></i>Area</span>
      <span><i class="dot" style="color:var(--blue)"></i>Chart</span>
    </div>
  </div>
  <svg width="916" height="287" viewBox="0 0 763 239" font-family="Open Sans, sans-serif" font-size="10" fill="#8d9298">
    <g stroke="#eef0f2" stroke-width="1">
      <line x1="79" y1="34" x2="720" y2="34"/><line x1="79" y1="71.5" x2="720" y2="71.5"/><line x1="79" y1="109" x2="720" y2="109"/><line x1="79" y1="146.5" x2="720" y2="146.5"/><line x1="79" y1="184" x2="720" y2="184"/>
      <line x1="79" y1="20" x2="79" y2="184"/><line x1="235" y1="20" x2="235" y2="184"/><line x1="392" y1="20" x2="392" y2="184"/><line x1="548" y1="20" x2="548" y2="184"/><line x1="704" y1="20" x2="704" y2="184"/>
    </g>
    <g text-anchor="end">
      <text x="45" y="37">200</text><text x="45" y="74.5">150</text><text x="45" y="112">100</text><text x="45" y="149.5">50</text><text x="45" y="187">0</text>
    </g>
    <g text-anchor="middle">
      <text x="81" y="218">2013</text><text x="237" y="218">2014</text><text x="392" y="218">2015</text><text x="548" y="218">2016</text><text x="704" y="218">2017</text>
    </g>
    <path d="M79,184 C130,120 155,109 184,109 C225,109 255,154 290,154 C360,154 430,60 480,60 C530,60 545,109 580,109 C620,109 640,105 660,95 C685,80 695,50 704,30 L704,184 Z" fill="#faa54b" fill-opacity=".7"/>
    <path d="M79,184 C150,140 200,105 240,105 C285,105 300,154 330,154 C400,154 460,79 540,79 C580,79 590,113 620,113 C660,113 690,90 704,53 L704,184 Z" fill="#33a6d7" fill-opacity=".7"/>
    <path d="M79,184 C120,150 140,131 170,131 C220,131 250,165 300,165 C360,165 380,79 420,79 C455,79 460,131 480,131 C520,131 530,100 555,100 C590,100 610,130 640,128 C675,125 690,110 704,71 L704,184 Z" fill="#886aae" fill-opacity=".72"/>
  </svg>
</section>

<section class="card" style="left:259px;top:546px;width:445px;height:354px">
  <div class="card-head">
    <span>PRODUCTIVITY OVERVIEW</span>
    <span class="range">Today <svg width="8" height="5" viewBox="0 0 8 5"><path d="M1 1l3 3 3-3" fill="none" stroke="#9a9fa5" stroke-width="1.2"/></svg></span>
  </div>
  <div class="donuts">
    <div class="donut">
      <div class="donut-ring">
        <svg width="116" height="116" viewBox="0 0 116 116"><circle cx="58" cy="58" r="52" fill="none" stroke="#e6e9ec" stroke-width="12"/><circle cx="58" cy="58" r="52" fill="none" stroke="#33a6d7" stroke-width="12" stroke-linecap="round" stroke-dasharray="241.8 326.7" transform="rotate(-90 58 58)"/></svg>
        <div class="donut-value" style="color:var(--blue)">74<sup>%</sup></div>
      </div>
      <div class="donut-label">Design</div>
    </div>
    <div class="donut">
      <div class="donut-ring">
        <svg width="116" height="116" viewBox="0 0 116 116"><circle cx="58" cy="58" r="52" fill="none" stroke="#e6e9ec" stroke-width="12"/><circle cx="58" cy="58" r="52" fill="none" stroke="#faa54b" stroke-width="12" stroke-linecap="round" stroke-dasharray="163.4 326.7" transform="rotate(-90 58 58)"/></svg>
        <div class="donut-value" style="color:var(--orange)">50<sup>%</sup></div>
      </div>
      <div class="donut-label">Front-end</div>
    </div>
    <div class="donut">
      <div class="donut-ring">
        <svg width="116" height="116" viewBox="0 0 116 116"><circle cx="58" cy="58" r="52" fill="none" stroke="#e6e9ec" stroke-width="12"/><circle cx="58" cy="58" r="52" fill="none" stroke="#86cfc6" stroke-width="12" stroke-linecap="round" stroke-dasharray="202.6 326.7" transform="rotate(-90 58 58)"/></svg>
        <div class="donut-value" style="color:var(--teal-light)">62<sup>%</sup></div>
      </div>
      <div class="donut-label">Back-end</div>
    </div>
  </div>
  <div class="note-rule"></div>
  <div class="note">
    <h4>Lorem Ipsum is simply dummy text</h4>
    <p>the printing and typesetting industry. lorem ipsum has been<br>the industry's standard dummy text ever</p>
  </div>
</section>

<section class="card" style="left:730px;top:546px;width:445px;height:354px">
  <div class="card-head">
    <span>PROGRESS BAR</span>
    <span class="range">Today <svg width="8" height="5" viewBox="0 0 8 5"><path d="M1 1l3 3 3-3" fill="none" stroke="#9a9fa5" stroke-width="1.2"/></svg></span>
  </div>
  <svg class="abs" style="left:0;top:43px" width="445" height="224" viewBox="0 0 371 187">
    <line x1="35" y1="20" x2="35" y2="186" stroke="#eef0f2"/>
    <line x1="20" y1="179" x2="352" y2="179" stroke="#eef0f2"/>
    <g fill="#f0f0f0">
      <rect x="49" y="28" width="14" height="151"/><rect x="77.5" y="28" width="14" height="151"/><rect x="106" y="28" width="14" height="151"/><rect x="134.5" y="28" width="14" height="151"/><rect x="163" y="28" width="14" height="151"/><rect x="191.5" y="28" width="14" height="151"/><rect x="220" y="28" width="14" height="151"/><rect x="248.5" y="28" width="14" height="151"/><rect x="277" y="28" width="14" height="151"/><rect x="305.5" y="28" width="14" height="151"/><rect x="334" y="28" width="14" height="151"/>
    </g>
    <g fill="#85cae6">
      <rect x="49" y="111" width="14" height="68"/><rect x="77.5" y="43" width="14" height="136"/><rect x="106" y="77" width="14" height="102"/><rect x="134.5" y="145" width="14" height="34"/><rect x="163" y="43" width="14" height="136"/><rect x="191.5" y="77" width="14" height="102"/><rect x="220" y="111" width="14" height="68"/><rect x="248.5" y="77" width="14" height="102"/><rect x="277" y="43" width="14" height="136"/><rect x="305.5" y="67" width="14" height="112"/><rect x="334" y="111" width="14" height="68"/>
    </g>
  </svg>
  <div class="total">$150,0000</div>
  <div class="delta"><span class="arrow">▲</span>1020 &nbsp;/&nbsp; <span class="arrow">▼</span>1020</div>
</section>

</body>
</html>
```